Quorvel Marketing & Design needs a Wordpress website

We need a wordpress design for a new marketing and design company in Australia called 'Quorvel Marketing & Design". The website needs to be responsive, modern, and attract new customers. It needs to be unique and different. We provide marketing and design solutions for small businesses from consulting, to flyer distribution to Pagebook ads etc. We would like to see designs that use the Quorvel logo colours. The final design should communicate professionalism, creativity & growth. It needs to stand out from the crowd.

Target Market(s)

Small Business who need a marketing freelancer to help them grow

Industry/Entity Type

Marketing

Number of Pages Required

3 page

Requirements
Must have
• Home page, services page & contact page

```html
<!DOCTYPE html>
<html lang="en">
<head>
<meta charset="utf-8">
<title>Quorvel Marketing &amp; Design</title>
<link href="https://fonts.googleapis.com/css2?family=Open+Sans:wght@400;600;700&family=Roboto:wght@400;500;700&display=swap" rel="stylesheet">
<style>
:root{
  --ink:#222;
  --muted:#555;
  --magenta:#c2185b;
  --navy:#2b2d6e;
  --navy-dark:#1b1c44;
  --black:#111;
  --card:#f1f1f3;
  --line:#ddd;
  --white:#fff;
}
*{box-sizing:border-box;margin:0;padding:0}
html,body{width:1200px;height:2308px;overflow:hidden}
body{font-family:"Open Sans",Arial,sans-serif;color:var(--ink);background:var(--white);position:relative}
.abs{position:absolute}
.topbar{left:48px;top:6px;font-size:11px;color:var(--muted)}
.brand{left:48px;top:22px;display:flex;align-items:center;gap:8px}
.brand .dot{width:18px;height:18px;border-radius:50%;background:var(--magenta)}
.brand span{font-family:"Roboto",sans-serif;font-weight:700;font-size:26px;color:var(--magenta)}
.tools{right:56px;top:8px;display:flex;gap:8px;align-items:center;font-size:11px;color:var(--muted)}
.tools i{display:block;width:12px;height:12px;background:#444}
.search{right:56px;top:40px;display:flex}
.search div{width:150px;height:22px;border:1px solid var(--line)}
.search b{width:36px;height:22px;background:var(--magenta)}
.nav{left:48px;top:68px;width:1104px;height:36px;background:var(--black);display:flex;justify-content:center;align-items:center;gap:4px}
.nav a{color:var(--white);text-decoration:none;font-size:13px;padding:10px 16px;font-family:"Roboto",sans-serif}
.nav a.on{background:var(--magenta)}
.hero{left:48px;top:104px;width:1104px;height:368px;background:linear-gradient(135deg,#8c8f96,#3d4048 55%,#6b6e76)}
.hero p{position:absolute;left:70px;top:306px;width:420px;color:var(--white);font-size:15px;line-height:1.35;text-shadow:0 1px 2px rgba(0,0,0,.6)}
.arrow{top:268px;width:22px;height:30px;background:rgba(255,255,255,.75)}
.card{top:500px;width:290px;height:428px;background:var(--card);border:1px solid var(--line)}
.card .pic{height:178px;margin:8px;background:linear-gradient(135deg,#5a7fb0,#c9d3e2)}
.card h3{font-size:13px;font-weight:700;margin:14px 14px 8px;color:var(--navy-dark)}
.card p{font-size:11.5px;line-height:1.5;color:var(--muted);margin:0 14px}
.plus{position:absolute;right:12px;bottom:12px;width:30px;height:30px;background:var(--navy);color:#fff;font-size:22px;line-height:30px;text-align:center}
.learn{left:0;top:952px;width:1200px;height:228px;background:linear-gradient(180deg,#2a2f44,#1b1e2c)}
.learn h2{position:absolute;top:34px;width:100%;text-align:center;color:var(--white);font-size:22px;font-weight:600}
.learn .field{position:absolute;left:200px;top:100px;width:620px;height:40px;background:var(--white)}
.learn .go{position:absolute;left:822px;top:100px;width:120px;height:40px;background:var(--navy);color:#fff;font-size:14px;font-weight:600;display:flex;align-items:center;justify-content:center}
.about h2,.services h2{font-family:"Roboto",sans-serif;font-weight:500}
.about{left:48px;top:1180px;width:1104px;height:230px}
.about h2{font-size:24px;margin-top:18px}
.about p{width:700px;font-size:12px;line-height:1.7;color:var(--muted);margin-top:10px}
.btn{display:inline-block;background:var(--navy-dark);color:#fff;font-size:11px;padding:7px 16px;margin-top:10px;margin-left:580px}
.about .pic{position:absolute;right:24px;top:12px;width:330px;height:212px;border:4px solid #e6e6ee;background:linear-gradient(135deg,#b8bdc8,#4c5361)}
.services{left:48px;top:1420px;width:1104px}
.services h2{font-size:34px;color:#7a4c87;margin-left:8px}
.svc{position:absolute;top:70px;width:300px}
.svc .pic{width:140px;height:110px;background:linear-gradient(135deg,#6d5aa8,#3d3487)}
.svc p{position:absolute;left:150px;top:0;width:150px;font-size:11px;line-height:1.45;color:var(--muted)}
.svc h4{font-weight:400;font-size:17px;color:#3a5da8;margin-top:12px}
.clients{left:0;top:1680px;width:1200px;height:320px;background:linear-gradient(135deg,#2b2f3c,#141620)}
.clients h2{position:absolute;left:48px;top:30px;color:#fff;font-size:26px;font-weight:600;letter-spacing:1px}
.clients p{position:absolute;left:48px;top:82px;width:680px;color:#e6e6e6;font-size:12px;line-height:1.65}
.clients .more{position:absolute;left:48px;top:252px;border:1px solid #fff;color:#fff;font-size:12px;padding:7px 14px}
.clients .pic{position:absolute;right:48px;top:60px;width:350px;height:250px;background:linear-gradient(135deg,#9aa1b0,#3c4250)}
.footer{left:0;top:2010px;width:1200px;height:252px;background:#0c0c0c;color:#fff}
.col{position:absolute;top:28px;font-size:12px}
.col h5{font-size:13px;font-weight:700;margin-bottom:14px}
.col li{list-style:none;margin-bottom:12px;color:#ccc;display:flex;align-items:center;gap:8px}
.col li i{width:18px;height:18px;background:var(--magenta);display:block}
.form label{display:block;color:#ccc;margin-bottom:6px;font-size:11px}
.form div{width:210px;height:18px;background:#fff;margin-bottom:6px}
.form .area{height:36px}
.form b{display:block;width:100px;height:22px;background:#2e6bd8;color:#fff;font-size:11px;text-align:center;line-height:22px;margin-left:110px;font-weight:600}
.bottom{left:0;top:2262px;width:1200px;height:46px;background:var(--navy-dark);color:#bbb;font-size:10px;padding:16px 48px}
</style>
</head>
<body>
<div class="abs topbar">Donate | Blog</div>
<div class="abs brand"><div class="dot"></div><span>Quorvel</span></div>
<div class="abs tools"><i></i><i></i><i></i><span>EN ▾</span></div>
<div class="abs search"><div></div><b></b></div>
<nav class="abs nav">
  <a class="on">Home</a><a>About Us</a><a>Marketing Consulting</a><a>Services</a><a>Teams and Conditions</a><a>Clients</a><a>Contact Us</a>
</nav>

<section class="abs hero" role="img" aria-label="Hand drawing a marketing strategy diagram with linked keywords">
  <p>It is a long established fact that a reader will be distracted by the readable content of a page when looking at its layout.</p>
</section>
<div class="abs arrow" style="left:52px"></div>
<div class="abs arrow" style="left:1126px"></div>

<article class="abs card" style="left:146px">
  <div class="pic" role="img" aria-label="Hands working over business charts"></div>
  <h3>LOREM IPSUM IS DUMMY</h3>
  <p>Lorem Ipsum is simply dummy text of the printing and typesetting industry. Lorem Ipsum has been the industry's standard dummy text ever since the 1500s, when an unknown printer took a galley of type and scrambled it.</p>
  <span class="plus">+</span>
</article>
<article class="abs card" style="left:455px">
  <div class="pic" role="img" aria-label="Team meeting around a laptop" style="background:linear-gradient(135deg,#d9a73c,#f3e2b7)"></div>
  <h3>LOREM IPSUM IS DUMMY</h3>
  <p>Lorem Ipsum is simply dummy text of the printing and typesetting industry. Lorem Ipsum has been the industry's standard dummy text ever since the 1500s, when an unknown printer took a galley of type and scrambled it.</p>
  <span class="plus">+</span>
</article>
<article class="abs card" style="left:764px">
  <div class="pic" role="img" aria-label="Business people reviewing documents" style="background:linear-gradient(135deg,#2d4f8a,#a6b4cc)"></div>
  <h3>LOREM IPSUM IS DUMMY</h3>
  <p>Lorem Ipsum is simply dummy text of the printing and typesetting industry. Lorem Ipsum has been the industry's standard dummy text ever since the 1500s, when an unknown printer took a galley of type and scrambled it.</p>
  <span class="plus">+</span>
</article>

<section class="abs learn" role="img" aria-label="Dim city skyline background">
  <h2>What You Want to Learn!</h2>
  <div class="field"></div>
  <div class="go">Click Here</div>
</section>

<section class="abs about">
  <h2>About Us</h2>
  <p>Lorem Ipsum is simply dummy text of the printing and typesetting industry. Lorem Ipsum has been the industry's standard dummy text ever since the 1500s, when an unknown printer took a galley of type and scrambled it to make a type specimen book. It has survived not only five centuries, but also the leap into electronic typesetting, remaining essentially unchanged. It was popularised in the 1960s with the release of Typeleaf sheets containing Lorem Ipsum passages, and more recently with desktop publishing software like Pressline Composer including versions of Lorem Ipsum.</p>
  <span class="btn">Read more</span>
  <div class="pic" role="img" aria-label="Business team walking together"></div>
</section>

<section class="abs services">
  <h2>OUR SERVICES</h2>
  <div class="svc" style="left:130px"><div class="pic" role="img" aria-label="Team icon on purple tile"></div><p>Lorem Ipsum is simply dummy text of the printing and typesetting industry. Lorem Ipsum has been the.</p><h4>Application Services</h4></div>
  <div class="svc" style="left:430px"><div class="pic" role="img" aria-label="Business person on purple tile"></div><p>Lorem Ipsum is simply dummy text of the printing and typesetting industry. Lorem Ipsum has been the.</p><h4>Application Services</h4></div>
  <div class="svc" style="left:730px"><div class="pic" role="img" aria-label="Growth chart on purple tile"></div><p>Lorem Ipsum is simply dummy text of the printing and typesetting industry. Lorem Ipsum has been the.</p><h4>Application Services</h4></div>
</section>

<section class="abs clients">
  <h2>OUR CLIENTS</h2>
  <p>Lorem Ipsum is simply dummy text of the printing and typesetting industry. Lorem Ipsum has been the industry's standard dummy text ever since the 1500s, when an unknown printer took a galley of type and scrambled it to make a type specimen book. It has survived not only five centuries, but also the leap into electronic typesetting, remaining essentially unchanged. It was popularised in the 1960s with the release of Typeleaf sheets containing Lorem Ipsum passages, and more recently with desktop publishing software like Pressline Composer including versions of Lorem Ipsum.</p>
  <span class="more">Read More</span>
  <div class="pic" role="img" aria-label="Smiling businessman in suit"></div>
</section>

<footer class="abs footer">
  <div class="col" style="left:160px"><h5>Quick Links</h5><ul><li>Home</li><li>Critical</li><li>Our Services</li><li>Courses</li></ul></div>
  <div class="col" style="left:380px"><h5>Information</h5><ul><li>Terms &amp; Regulations</li><li>Summary</li><li>Contact</li><li>Agent Form</li></ul></div>
  <div class="col form" style="left:600px"><h5>Contact Detail</h5>
    <label>Name</label><div></div><label>Email</label><div></div><label>Message</label><div class="area"></div><b>Submit</b></div>
  <div class="col" style="left:940px"><h5>Follow Us on</h5><ul><li><i></i>Pagebook</li><li><i></i>Chirper</li><li><i></i>ViewTube</li><li><i></i>Blog</li></ul></div>
</footer>
<div class="abs bottom">© 2015 Quorvel. All rights reserved.</div>
</body>
</html>
```